PRESENTATION FOLDER DESIGN

I would like to design a presentation folder that is 6 x 9 with 2 x 4 inch pockets.
I have attached the logo to use as well as the template for the presentation folder.

I also included the front and back of the business cards so that you can see the overall look I am trying to go for as well as the information to have on there.

The presentation folder will be used to send out an invitation to a conference for dentists.

Target Market(s)

dentists

Font styles to use
Sans Serif

Requirements
Must have
• The clours must be the same as on the logo.
• On the cover, I would like a title in bold large letters that says:
• PLEASE JOIN US FOR OUR EXCLUSIVE EVENTS
• FOR DENTAL PROFESSIONALS
• *eligible for CE credits
• I would like to have this picture on the cover as well.
• ON THE BACK, i WOULD THE COLOURS TO BE THE BLUE FROM THE LOGO AND THE WRITING IN WHITE.
• THE INSIDE FLAPS MUST BE IN THE BLUE BUT THE INSIDE OF THE FOLDER SHOULD BE IN ORANGE.
• ON THE INSIDE FLAPS WE SHOULD WRITE:
• ON THE LEFT FLAP: I WANT TO PURCHASE A CLINIC
• ON THE RIGHT FLAP: I WANT TO SELL MY CLINIC

```html
<!DOCTYPE html>
<html lang="en">
<head>
<meta charset="utf-8">
<title>Presentation Folder – Inside Spread</title>
<link rel="stylesheet" href="https://fonts.googleapis.com/css2?family=Didact+Gothic&family=Montserrat:wght@700&display=swap">
<style>
  :root {
    --board: #4d4f4c;
    --board-label: #5f615e;
    --orange: #f26722;
    --orange-deep: #d2591b;
    --orange-fold: #df5e1e;
    --pocket-blue: #6dcff6;
    --white: #ffffff;
  }
  * { margin: 0; padding: 0; box-sizing: border-box; }
  html, body {
    width: 1200px;
    height: 929px;
    overflow: hidden;
    background: var(--board);
  }
  .board {
    position: relative;
    width: 1200px;
    height: 929px;
  }
  .board-label {
    position: absolute;
    left: 868px;
    top: 22px;
    font-family: "Didact Gothic", sans-serif;
    font-size: 74px;
    line-height: 1;
    color: var(--board-label);
  }
  .folder {
    position: absolute;
    left: 136px;
    top: 116px;
    width: 930px;
    height: 697px;
    box-shadow: 5px 5px 7px rgba(0, 0, 0, 0.55);
  }
  .folder-art {
    position: absolute;
    inset: 0;
    display: block;
  }
  .pocket-label {
    position: absolute;
    top: 484px;
    width: 400px;
    text-align: center;
    color: var(--white);
    transform: translateX(-50%);
  }
  .pocket-label--left { left: 213px; }
  .pocket-label--right { left: 711px; }
  .brand-name {
    font-family: "Montserrat", sans-serif;
    font-weight: 700;
    font-size: 26px;
    letter-spacing: 3px;
    line-height: 1;
    margin-bottom: 28px;
  }
  .pocket-lead {
    font-family: "Montserrat", sans-serif;
    font-weight: 700;
    font-size: 31px;
    line-height: 1.05;
  }
  .pocket-action {
    font-family: "Didact Gothic", sans-serif;
    font-size: 33px;
    line-height: 1.05;
  }
</style>
</head>
<body>
<div class="board">
  <div class="board-label">Inside</div>

  <div class="folder">
    <svg class="folder-art" width="930" height="697" viewBox="0 0 930 697" aria-hidden="true">
      <defs>
        <linearGradient id="panel-left" x1="0" x2="1" y1="0" y2="0">
          <stop offset="0" stop-color="var(--orange-deep)"/>
          <stop offset="0.55" stop-color="var(--orange)"/>
          <stop offset="1" stop-color="var(--orange)"/>
        </linearGradient>
        <linearGradient id="panel-right" x1="0" x2="1" y1="0" y2="0">
          <stop offset="0" stop-color="var(--orange-fold)"/>
          <stop offset="0.3" stop-color="var(--orange)"/>
          <stop offset="1" stop-color="var(--orange)"/>
        </linearGradient>
      </defs>
      <rect class="inside-left" x="0" y="0" width="465" height="697" fill="url(#panel-left)"/>
      <rect class="inside-right" x="465" y="0" width="465" height="697" fill="url(#panel-right)"/>
      <path class="pocket pocket-left" d="M0 393 H376 Q415 393 419 436 L449 697 H0 Z" fill="var(--pocket-blue)"/>
      <path class="pocket pocket-right" d="M930 393 H552 Q514 393 510 436 L479 697 H930 Z" fill="var(--pocket-blue)"/>
    </svg>

    <div class="pocket-label pocket-label--left">
      <div class="brand-name">RIDGELINE</div>
      <div class="pocket-lead">I WANT TO</div>
      <div class="pocket-action">PURCHASE A CLINIC</div>
    </div>

    <div class="pocket-label pocket-label--right">
      <div class="brand-name">RIDGELINE</div>
      <div class="pocket-lead">I WANT TO</div>
      <div class="pocket-action">SELL MY CLINIC</div>
    </div>
  </div>
</div>
</body>
</html>
```